'Brantley Electrical' web design

I need a web design for an electrical/electrician company based in sydney called brantley electrical. The logo design and business card design have been uploaded to be used on the web design. I want the design to be very modern and clean. I want the sector designs on the business card, i.e "residential", "commercial" etc, to be fleshed out on the front page. Base those sector designs off the business card but try to make them more minimal and modern to suit the website. Contact details are also on the business card. Try to suit the colour scheme of the logo. The sector designs should be up the top and linked so when clicked it will scroll down the website to brief descriptions of the work the company does in those sectors. I want the website to mainly attract builders, insurance companies and the commercial sector. I want the website to look unique. Custom graphics would be nice to make the website standout. I don't want the website to look like generic.

Target Market(s)

Builders, commercial sector, home owners

Industry/Entity Type

Electrical/Construction

Coding

Coded - Design and coding required

Number of Pages Required

3 page

Requirements
Must have
• Modern design
Nice to have
• Custom graphics that make the website unique

```html
<!DOCTYPE html>
<html lang="en">
<head>
<meta charset="utf-8">
<title>Brantley Electrical – Powering Your Projects</title>
<link href="https://fonts.googleapis.com/css2?family=Montserrat:wght@600;700;800&family=Poppins:wght@400;500;600&display=swap" rel="stylesheet">
<style>
:root{
  --navy:#0c0b4f;
  --navy-deep:#090a45;
  --blue:#0d5ba8;
  --orange:#ea8549;
  --yellow:#fccc0b;
  --ink:#3a3a4a;
  --pale:#eef5fd;
  --ring:#dfeafb;
  --white:#ffffff;
}
*{margin:0;padding:0;box-sizing:border-box}
html,body{width:1200px;height:2630px;overflow:hidden;background:var(--white)}
body{font-family:"Poppins",sans-serif;color:var(--ink)}
.page{position:relative;width:1200px;height:2630px;overflow:hidden}
.abs{position:absolute}
.btn{position:absolute;display:flex;align-items:center;justify-content:center;background:var(--yellow);color:var(--navy);font-family:"Poppins",sans-serif;font-weight:600;font-size:14px;border-radius:20px;text-decoration:none}

/* hero */
.hero{position:absolute;left:0;top:0;width:1200px;height:676px;background:linear-gradient(180deg,#0b0a4c 0%,#26134a 35%,#5a3050 70%,#8c524c 100%);border-bottom:3px solid #2a4a8a}
.brand{position:absolute;font-family:"Montserrat",sans-serif;font-weight:800;color:var(--white);white-space:nowrap}
.brand-header{left:61px;top:30px;font-size:22px;display:flex;align-items:center;gap:10px}
.brand-dot{width:14px;height:14px;border-radius:50%;background:var(--orange)}
.phone-btn{left:931px;top:23px;width:154px;height:37px;gap:8px;font-size:13.5px}
.menu{position:absolute;left:1116px;top:30px;width:24px;height:20px;display:flex;flex-direction:column;justify-content:space-between}
.menu span{display:block;height:3px;background:var(--white);border-radius:2px}
.hero-title{left:61px;top:290px;font-size:52px;letter-spacing:-.5px}
.hero-tagline{position:absolute;left:62px;top:366px;color:var(--white);font-size:15px;letter-spacing:6.2px}
.hero-btn{left:61px;top:427px;width:175px;height:37px}
.hero-art{position:absolute;left:439px;top:148px;width:761px;height:525px;background:linear-gradient(160deg,rgba(166,182,240,.35),rgba(240,140,70,.25) 60%,rgba(40,70,160,.35));border-radius:8px 0 0 0}

/* services */
.section-title{position:absolute;left:0;width:1200px;top:768px;text-align:center;font-family:"Montserrat",sans-serif;font-weight:800;font-size:36px;color:var(--blue)}
.section-title .accent{color:var(--orange)}
.band-pale{position:absolute;left:0;top:1393px;width:1200px;height:582px;background:var(--pale)}
.service-ring{position:absolute;width:462px;height:462px;border-radius:50%;background:var(--ring)}
.service-art{position:absolute;left:17px;top:17px;width:428px;height:428px;border-radius:50%}
.art-residential{background:linear-gradient(180deg,#2a1a4e 0%,#6b5a72 35%,#c9c8b4 65%,#5aa8d8 100%)}
.art-commercial{background:linear-gradient(180deg,#24164e 0%,#6a4a6a 45%,#e4684e 75%,#f08a5a 100%)}
.service-name{position:absolute;font-family:"Montserrat",sans-serif;font-weight:800;font-size:30px;color:var(--blue)}
.service-copy{position:absolute;width:490px;font-size:14.2px;line-height:22.5px}
.service-copy p+p{margin-top:9px}

/* call to action */
.cta-title{position:absolute;left:0;top:2040px;width:1200px;text-align:center;font-family:"Montserrat",sans-serif;font-weight:700;font-size:38.5px;line-height:44px;color:var(--navy)}
.cta-title .accent{color:var(--orange)}
.cta-copy{position:absolute;left:0;top:2144px;width:1200px;text-align:center;font-size:14.2px;line-height:22.5px}
.cta-btn{left:523px;top:2219px;width:176px;height:37px}

/* footer */
.footer{position:absolute;left:0;top:2334px;width:1200px;height:296px;background:var(--navy-deep);color:var(--white)}
.brand-footer{left:0;width:1200px;top:55px;text-align:center;font-size:26px}
.contact{position:absolute;top:124px;width:220px;text-align:center;font-size:14.2px;line-height:22.5px}
.contact-icon{width:38px;height:38px;border:1px solid var(--white);border-radius:50%;margin:0 auto 25px;display:flex;align-items:center;justify-content:center}
.contact strong{font-weight:600}
.footer-rule{position:absolute;left:0;top:260px;width:1200px;height:1px;background:rgba(255,255,255,.18)}
.copyright{position:absolute;left:0;top:268px;width:1200px;text-align:center;font-size:12.5px}
.copyright strong{font-weight:600}
</style>
</head>
<body>
<div class="page">

  <header class="hero">
    <div class="brand brand-header"><span class="brand-dot"></span>BRANTLEY ELECTRICAL</div>
    <a class="btn phone-btn" href="#">
      <svg width="16" height="16" viewBox="0 0 24 24" fill="none" stroke="#0c0b4f" stroke-width="2.2" stroke-linecap="round" stroke-linejoin="round"><path d="M22 16.9v3a2 2 0 0 1-2.2 2 19.8 19.8 0 0 1-8.6-3.1 19.5 19.5 0 0 1-6-6A19.8 19.8 0 0 1 2.1 4.2 2 2 0 0 1 4.1 2h3a2 2 0 0 1 2 1.7c.1 1 .4 1.9.7 2.8a2 2 0 0 1-.5 2.1L8 9.9a16 16 0 0 0 6 6l1.3-1.3a2 2 0 0 1 2.1-.4c.9.3 1.8.6 2.8.7a2 2 0 0 1 1.8 2z"/></svg>
      +0400 318 264
    </a>
    <div class="menu" aria-label="Menu"><span></span><span></span><span></span></div>

    <h1 class="brand hero-title">BRANTLEY ELECTRICAL</h1>
    <p class="hero-tagline">POWERING YOUR PROJECTS</p>
    <a class="btn hero-btn" href="#">Get A Free Quote</a>

    <div class="hero-art" role="img" aria-label="Illustration of electricians working on power poles, transmission towers and solar panels"></div>
  </header>

  <h2 class="section-title">WHAT <span class="accent">WE DO</span></h2>

  <section class="service">
    <div class="service-ring" style="left:60px;top:855px">
      <div class="service-art art-residential" role="img" aria-label="Illustration of a modern two-storey house"></div>
    </div>
    <h3 class="service-name" style="left:628px;top:914px">RESIDENTIAL</h3>
    <div class="service-copy" style="left:628px;top:956px">
      <p>Lorem Ipsum is simply dummy text of the printing and typesetting industry. Lorem Ipsum has been the industry's standard dummy text ever since the 1500s, when an unknown printer took a galley of type and scrambled it to make a type specimen book. It has survived not only five centuries, but also the leap into electronic typesetting, remaining essentially unchanged. It was popularised in the 1960s with the release of Letraset sheets containing</p>
      <p>Lorem Ipsum passages, and more recently with desktop publishing software like Aldus PageMaker including versions of Lorem Ipsum.</p>
    </div>
    <a class="btn" href="#" style="left:627px;top:1193px;width:135px;height:37px">Learn More</a>
  </section>

  <div class="band-pale"></div>
  <section class="service">
    <h3 class="service-name" style="left:61px;top:1530px">COMMERCIAL</h3>
    <div class="service-copy" style="left:61px;top:1572px">
      <p>Lorem Ipsum is simply dummy text of the printing and typesetting industry. Lorem Ipsum has been the industry's standard dummy text ever since the 1500s, when an unknown printer took a galley of type and scrambled it to make a type specimen book. It has survived not only five centuries, but also the leap into electronic typesetting, remaining essentially unchanged. It was popularised in the 1960s with the release of Letraset sheets containing</p>
      <p>Lorem Ipsum passages, and more recently with desktop publishing software like Aldus PageMaker including versions of Lorem Ipsum.</p>
    </div>
    <a class="btn" href="#" style="left:60px;top:1809px;width:135px;height:37px">Learn More</a>
    <div class="service-ring" style="left:663px;top:1453px">
      <div class="service-art art-commercial" role="img" aria-label="Illustration of a city skyline with office towers"></div>
    </div>
  </section>

  <section class="cta">
    <h2 class="cta-title">Lorem Ipsum is simply dummy text of<br>the printing <span class="accent">and typesetting industry.</span></h2>
    <p class="cta-copy">Lorem Ipsum is simply dummy text of the printing and typesetting industry. Lorem Ipsum has been<br>the industry's standard dummy text ever since the 1500s, when an unknown printer.</p>
    <a class="btn cta-btn" href="#">Get A Free Quote</a>
  </section>

  <footer class="footer">
    <div class="brand brand-footer">BRANTLEY ELECTRICAL</div>

    <div class="contact" style="left:302px">
      <div class="contact-icon"><svg width="18" height="18" viewBox="0 0 24 24" fill="none" stroke="#fccc0b" stroke-width="2" stroke-linecap="round" stroke-linejoin="round"><path d="M12 22s7-6.5 7-12a7 7 0 0 0-14 0c0 5.5 7 12 7 12z"/><circle cx="12" cy="10" r="2.5"/></svg></div>
      123 ,Lorem Ipsum Is a dummy<br>text.
    </div>
    <div class="contact" style="left:488px">
      <div class="contact-icon"><svg width="18" height="18" viewBox="0 0 24 24" fill="none" stroke="#fccc0b" stroke-width="2" stroke-linecap="round" stroke-linejoin="round"><path d="M22 16.9v3a2 2 0 0 1-2.2 2 19.8 19.8 0 0 1-8.6-3.1 19.5 19.5 0 0 1-6-6A19.8 19.8 0 0 1 2.1 4.2 2 2 0 0 1 4.1 2h3a2 2 0 0 1 2 1.7c.1 1 .4 1.9.7 2.8a2 2 0 0 1-.5 2.1L8 9.9a16 16 0 0 0 6 6l1.3-1.3a2 2 0 0 1 2.1-.4c.9.3 1.8.6 2.8.7a2 2 0 0 1 1.8 2z"/></svg></div>
      <strong>+0400 318 264</strong>
    </div>
    <div class="contact" style="left:660px;width:260px">
      <div class="contact-icon"><svg width="18" height="18" viewBox="0 0 24 24" fill="none" stroke="#fccc0b" stroke-width="2" stroke-linecap="round" stroke-linejoin="round"><rect x="3" y="5" width="18" height="14" rx="2"/><path d="M3 7l9 6 9-6"/></svg></div>
      info@brantleyelectrical.com.au
    </div>

    <div class="footer-rule"></div>
    <p class="copyright">© Copyright 2023 <strong>BRANTLEY ELECTRICAL</strong> All Right Reserved.</p>
  </footer>

</div>
</body>
</html>
```